IT Company WebPage Relaunch looking for modern and clean approach

We are looking to relaunch our website, to give it a more modern and clean look.
Company Background:
With nearly 20 years of industry expertise, we've been committed to delivering top-notch professional services and products, ensuring client success and efficiency. Our mission is to provide clients with talented human and technological resources, employing industry best practices for effective solutions. We envision becoming a pivotal player in Dominican Republic's Techonology sector, expanding our footprint across the Caribbean Central America and USA
Design Objectives:
1. Brand Identity: The website should reflect our brand identity based in our logo, color scheme, and overall aesthetic. Consistency with existing brand materials is essential.
2. User Experience: Prioritize user experience by ensuring easy navigation and intuitive layout. The website should be accessible and responsive across various devices and screen sizes.
3. Content Presentation: Present our content (text, images, videos) in a visually appealing and organized manner. Use creative layouts and typography to enhance readability and engagement.
4. Functionality: Implement necessary features and functionalities to support our business objectives. This may include contact form.
5. SEO Optimization: Design the website with search engine optimization (SEO) best practices in mind to improve visibility and ranking on search engine results pages (SERPs).
6. Multilanguage: Spanish and English
Pages and Sections:
1. Home Page:
o Welcome message/introduction
o Highlights of key products/services
o Clear navigation to other sections/pages
o Metrics (10 Satisfied customer) (Services provided in 5 countries) etc.
2. About Us:
o Company overview
o Mission, vision, and values
o Team/Staff profiles (tentative)
3. Products/Services:
o Our Partners
o Detailed descriptions of products/services offered
o Images/videos
4. Portfolio/Projects:
o Our Customers
o Case Studies
o Customer’s testimonials
5. Blog/News:
o Platform for sharing industry insights, updates, or company news
o Categories/tags for easy browsing
6. Contact Us:
o Contact form
o Company address, phone number, email
o Social media links
Design Preferences:
• Clean and modern design aesthetic
• Use of whitespace to enhance readability and visual appeal
• High-quality images and graphics
• Responsive to multiple devices
Technical Requirements:
• Compatibility with major web browsers (Chrome, Firefox, Safari, Edge)
• Compliance with web standards and best practices
Current Website:
https://www.quorvanta.com.do
Note: The website should not be on Wordpress, we want an html/css website.

```html
<!DOCTYPE html>
<html lang="en">
<head>
<meta charset="utf-8">
<title>Quorvanta — IT Consulting and Services</title>
<link rel="stylesheet" href="https://fonts.googleapis.com/css2?family=Rajdhani:wght@400;500;600;700&display=swap">
<style>
:root{
  --orange:#f7941d;
  --orange-deep:#f26a2a;
  --yellow:#fbb917;
  --red:#e0312f;
  --ink:#1f2226;
  --navy:#03161c;
  --grey:#6b6f74;
  --line:#e6e6e6;
  --foot-top:#4b4b4b;
  --foot-bot:#161616;
}
*{box-sizing:border-box;margin:0;padding:0}
html,body{width:1200px;height:3127px;overflow:hidden}
body{position:relative;background:#fff;font-family:"Rajdhani",sans-serif;color:var(--ink)}
.abs{position:absolute}
.topline{left:0;top:0;width:1200px;height:4px;background:var(--orange)}

/* header */
.brand{display:flex;align-items:center;gap:10px}
.brand-dot{width:34px;height:34px;border-radius:50%;background:var(--orange)}
.brand-name{font-weight:700;font-size:30px;line-height:1;letter-spacing:.5px;color:var(--ink)}
.brand-tag{font-weight:600;font-size:11px;letter-spacing:.4px;color:var(--ink);margin-top:2px}
.header-brand{left:146px;top:20px}
.phone-pill{left:755px;top:0;width:231px;height:39px;background:var(--orange);border-radius:0 0 24px 24px;color:#fff;font-weight:700;font-size:23px;display:flex;align-items:center;justify-content:center;gap:8px}
.phone-ic{width:22px;height:22px;border-radius:50%;background:#fff;display:flex;align-items:center;justify-content:center}
.socials{display:flex;gap:6px}
.socials span{width:17px;height:17px;border-radius:50%;border:1.5px solid #9aa6c7;display:block}
.header-socials{left:625px;top:16px}
.nav{left:514px;top:52px;display:flex;gap:28px;font-weight:700;font-size:12.5px;letter-spacing:.3px}
.nav .lang{display:flex;gap:4px;align-items:center}

/* hero */
.hero{left:7px;top:80px;width:1186px;height:485px;background:var(--navy);border-radius:60px 220px 300px 60px/60px 200px 210px 60px;overflow:hidden}
.hero-photo{left:0;top:0;width:560px;height:485px;background:radial-gradient(circle at 45% 40%,#3a5a7a 0%,#1b2c3c 40%,rgba(3,22,28,0) 75%),linear-gradient(90deg,#2a3440 0%,#1a2530 60%,rgba(3,22,28,0) 100%)}
.hero-title{left:590px;top:168px;font-weight:700;font-size:50px;line-height:58px;color:#fff;letter-spacing:.5px}
.hero-title .accent{color:var(--red);font-weight:500}
.btn{display:flex;align-items:center;gap:10px;background:linear-gradient(90deg,var(--orange-deep),var(--orange));color:#fff;font-weight:700;font-size:14px;border-radius:6px 24px 24px 6px;padding:0 6px 0 18px}
.btn i{width:30px;height:30px;border-radius:50%;background:#fff;display:flex;align-items:center;justify-content:center}
.hero-btn{left:590px;top:364px;height:46px}
.hero-play{left:1072px;top:423px;width:30px;height:30px;border-radius:50%;background:var(--red);display:flex;align-items:center;justify-content:center}

/* about */
.about-panel{left:143px;top:482px;width:900px;height:420px;background:#fff;border-radius:100px 120px 0 0}
.eyebrow{font-weight:700;font-size:21px;color:var(--orange)}
.about-eyebrow{left:197px;top:530px}
.about-title{left:197px;top:557px;font-weight:700;font-size:44px;color:var(--ink)}
.about-title span{color:var(--red)}
.about-text{left:197px;top:616px;width:402px;font-size:15px;line-height:22.5px;color:var(--grey);text-align:justify}
.about-btn{left:197px;top:799px;height:46px}
.emblem{left:705px;top:515px;width:340px;height:340px;border-radius:50%;background:radial-gradient(circle at 40% 40%,#f2f2f2 0%,#c9c9c9 35%,#e94a2c 60%,#f7941d 80%,rgba(255,255,255,0) 81%)}
.stat{background:#fff;border-radius:30px;box-shadow:0 6px 18px rgba(0,0,0,.12);display:flex;align-items:center;gap:10px;padding:0 16px;font-weight:600;font-size:12px;line-height:15px}
.stat b{color:var(--red);font-size:19px}
.stat-countries{left:893px;top:708px;width:161px;height:57px}
.stat-customers{left:634px;top:771px;width:162px;height:57px}

/* features */
.feature{width:142px;height:142px;transform:rotate(45deg);background:#fff;box-shadow:0 10px 30px rgba(0,0,0,.08)}
.feature.active{border:2px solid var(--orange);box-shadow:none}
.feature-label{width:180px;text-align:center;font-weight:700;font-size:16px;line-height:19px;color:var(--ink)}
.feature-label svg{display:block;margin:0 auto 14px}

/* products */
.products{left:16px;top:1134px;width:1168px;height:508px;background:linear-gradient(180deg,var(--orange) 0%,var(--yellow) 100%);border-radius:180px 100px 120px 200px/180px 100px 120px 200px}
.products-title{left:0;top:1204px;width:1200px;text-align:center;font-weight:700;font-size:44px;color:#fff}
.svc-title{font-weight:700;font-size:15px;color:#fff}
.svc-text{font-size:11.5px;line-height:15.5px;color:#fff}
.svc-link{font-weight:700;font-size:10.5px;color:#fff;text-decoration:underline}
.r{text-align:right}
.svc-ic{width:62px;height:62px;border-radius:50%;background:#fff;border:5px solid var(--yellow);display:flex;align-items:center;justify-content:center}
.svc-ic span{width:44px;height:44px;border-radius:50%;background:var(--yellow);display:flex;align-items:center;justify-content:center}
.dome{left:450px;top:1482px;width:300px;height:300px;border-radius:50%;background:#fff;border:14px solid #fff;box-shadow:0 0 0 3px var(--yellow)}
.dome-mark{left:540px;top:1530px;width:120px;height:120px;border-radius:50%;background:linear-gradient(135deg,var(--red),var(--orange))}

/* portfolio */
.section-title{left:0;width:1200px;text-align:center;font-weight:700;font-size:42px;color:var(--ink)}
.section-title span{color:var(--red)}
.partner{top:1828px;width:202px;height:95px;border:2px solid var(--line);border-radius:3px;display:flex;align-items:center;justify-content:center;font-weight:700;font-size:24px;color:var(--ink);letter-spacing:.5px}
.arrow{width:38px;height:38px;border-radius:50%;border:1.5px solid #bbb;display:flex;align-items:center;justify-content:center}

/* blog */
.card{top:2083px;width:281px;height:411px;background:#fff;box-shadow:0 4px 14px rgba(0,0,0,.12);text-align:center}
.card.featured{background:linear-gradient(180deg,var(--orange-deep),var(--red))}
.card-img{margin:4px;height:182px}
.card-date{margin-top:20px;display:flex;align-items:center;justify-content:center;gap:7px;font-weight:700;font-size:12.5px;color:var(--orange)}
.card-date i{width:22px;height:22px;border-radius:50%;border:1.5px solid var(--orange);display:block}
.card-title{margin:14px 22px 0;font-weight:700;font-size:16px;line-height:21px}
.card-text{margin:14px 22px 0;font-size:13.5px;line-height:20.5px;color:var(--grey);text-align:justify;text-align-last:center}
.card.featured .card-date,.card.featured .card-title,.card.featured .card-text{color:#fff}
.card.featured .card-date i{border-color:#fff}

/* testimonials + footer */
.footer{left:0;top:2658px;width:1200px;height:469px;background:linear-gradient(180deg,var(--foot-top),var(--foot-bot))}
.testi{left:143px;top:2598px;width:911px;height:160px;background:#fff;border-radius:70px 70px 90px 90px;border-bottom:3px solid var(--orange-deep)}
.testi-title{left:231px;top:2622px;font-weight:700;font-size:42px}
.testi-quote{left:560px;top:2630px;width:430px;font-style:italic;font-size:17px;line-height:24px;color:var(--grey)}
.foot-brand .brand-dot{width:58px;height:58px;background:#fff}
.foot-brand .brand-name{color:#fff;font-size:46px}
.foot-brand .brand-tag{color:#fff;font-size:17px}
.contact-line{display:flex;align-items:center;gap:12px;color:#fff}
.contact-line i{width:28px;height:28px;border-radius:50%;display:flex;align-items:center;justify-content:center}
.copy{left:150px;top:3022px;color:#fff;font-size:14px}
.form-title{left:628px;top:2838px;font-weight:700;font-size:22px;color:var(--orange)}
.field{background:#fff;font-size:10.5px;color:#999;padding:9px 12px}
.foot-socials span{width:25px;height:25px;border-color:#fff;border-width:2px}
</style>
</head>
<body>
<div class="abs topline"></div>

<header>
  <div class="abs brand header-brand">
    <span class="brand-dot"></span>
    <div><div class="brand-name">QUORVANTA</div><div class="brand-tag">IT CONSULTING AND SERVICES</div></div>
  </div>
  <div class="abs socials header-socials"><span></span><span></span><span></span><span></span><span></span></div>
  <div class="abs phone-pill"><span class="phone-ic"><svg width="12" height="12" viewBox="0 0 24 24"><path fill="#f7941d" d="M6.6 10.8a15 15 0 0 0 6.6 6.6l2.2-2.2c.3-.3.7-.4 1-.2 1.1.4 2.3.6 3.6.6.6 0 1 .4 1 1V20c0 .6-.4 1-1 1A17 17 0 0 1 3 4c0-.6.4-1 1-1h3.5c.6 0 1 .4 1 1 0 1.3.2 2.5.6 3.6.1.3 0 .7-.2 1z"/></svg></span>809-555-0172</div>
  <nav class="abs nav">
    <span>▸HOME</span><span>ABOUT US</span><span>PRODUCTS</span><span>PORTFOLIO</span><span>BLOG</span><span>CONTACT US</span><span class="lang">EN ▾</span>
  </nav>
</header>

<section>
  <div class="abs hero">
    <div class="abs hero-photo" role="img" aria-label="Hand reaching toward a glowing network globe surrounded by people icons"></div>
  </div>
  <h1 class="abs hero-title">THE REVOLUTION<br><span class="accent">TECHNOLOGY:A LOOK</span><br>INTO THE FUTURE</h1>
  <div class="abs btn hero-btn">CONTACT US <i><svg width="12" height="12" viewBox="0 0 10 10"><path d="M2 1l7 4-7 4z" fill="#f26a2a"/></svg></i></div>
  <div class="abs hero-play"><svg width="12" height="12" viewBox="0 0 10 10"><path d="M2 1l7 4-7 4z" fill="#fff"/></svg></div>
</section>

<section>
  <div class="abs about-panel"></div>
  <div class="abs eyebrow about-eyebrow">ABOUT</div>
  <h2 class="abs about-title">QUORV<span>ANTA</span></h2>
  <p class="abs about-text">With a history of almost two decades in the market, Quorvanta stands out for providing professional services and technological solutions that optimize its clients' processes, thus driving their growth. Our team is made up of experts in various areas, such as software development, service management, information security and API administration, guaranteeing a comprehensive and cutting-edge approach for each project.</p>
  <div class="abs btn about-btn">READ MORE <i><svg width="12" height="12" viewBox="0 0 10 10"><path d="M2 1l7 4-7 4z" fill="#f26a2a"/></svg></i></div>
  <div class="abs emblem" role="img" aria-label="Large brand emblem artwork in red, orange and silver"></div>
  <div class="abs" style="left:674px;top:634px;width:15px;height:15px;border:2px solid var(--red);transform:rotate(45deg)"></div>
  <div class="abs" style="left:1068px;top:715px;width:15px;height:15px;background:#ccc;transform:rotate(45deg)"></div>
  <div class="abs" style="left:78px;top:741px;width:15px;height:15px;background:#fde27a;transform:rotate(45deg)"></div>
  <div class="abs stat stat-countries"><svg width="20" height="18" viewBox="0 0 20 18"><path d="M1 3l6-2 6 2 6-2v14l-6 2-6-2-6 2z" fill="#f7941d"/></svg><div>Services provided<br>in <b>5</b> countries</div></div>
  <div class="abs stat stat-customers"><svg width="18" height="18" viewBox="0 0 24 24"><path d="M12 2l3 7 7 .6-5.3 4.6 1.6 7.3L12 17.8 5.7 21.5l1.6-7.3L2 9.6 9 9z" fill="#f7941d"/></svg><div><b>10</b><br>Satisfied customer</div></div>
</section>

<section>
  <div class="abs feature" style="left:174px;top:913px"></div>
  <div class="abs feature active" style="left:411px;top:913px"></div>
  <div class="abs feature" style="left:647px;top:913px"></div>
  <div class="abs feature" style="left:884px;top:913px"></div>
  <div class="abs feature-label" style="left:155px;top:932px"><svg width="42" height="42" viewBox="0 0 24 24" fill="none" stroke="#e94a2c" stroke-width="2.4"><path d="M4 12a8 8 0 1 0 2.5-5.8"/><path d="M4 3v5h5"/><path d="M12 8v4l3 2"/></svg>KNOWLEDGE<br>TRANSFER</div>
  <div class="abs feature-label" style="left:392px;top:932px"><svg width="42" height="42" viewBox="0 0 24 24" fill="none" stroke="#f7941d" stroke-width="2.4"><rect x="9" y="2" width="6" height="12" rx="3" fill="#f7941d"/><path d="M5 11a7 7 0 0 0 14 0M12 18v4"/></svg>TECHNICAL<br>SUPPORT</div>
  <div class="abs feature-label" style="left:628px;top:932px"><svg width="42" height="42" viewBox="0 0 24 24" fill="#f7941d"><circle cx="12" cy="7" r="5"/><path d="M3 22a9 7 0 0 1 18 0z"/></svg>PROFESSIONAL<br>SERVICES</div>
  <div class="abs feature-label" style="left:865px;top:932px"><svg width="42" height="42" viewBox="0 0 24 24" fill="#e94a2c"><path d="M3 22V10l9-6 9 6v12h-6v-6H9v6z"/></svg>EDUCATION</div>
</section>

<section>
  <div class="abs products"></div>
  <h2 class="abs products-title">PRODUCTS AND SERVICES</h2>
  <svg class="abs" style="left:0;top:0" width="1200" height="1700">
    <g stroke="#fff" stroke-width="2" fill="#fff">
      <line x1="524" y1="1430" x2="541" y2="1486"/>
      <line x1="660" y1="1430" x2="640" y2="1482"/>
      <line x1="448" y1="1505" x2="486" y2="1524"/>
      <line x1="752" y1="1512" x2="722" y2="1535"/>
      <circle cx="524" cy="1430" r="4"/><circle cx="660" cy="1430" r="4"/><circle cx="448" cy="1505" r="4"/><circle cx="752" cy="1512" r="4"/>
    </g>
  </svg>
  <div class="abs dome"></div>
  <div class="abs" style="left:420px;top:1642px;width:360px;height:160px;background:#fff"></div>
  <div class="abs dome-mark"></div>

  <div class="abs r" style="left:220px;top:1331px;width:243px"><div class="svc-title">SERVICE MANAGEMENT</div><p class="svc-text" style="margin-top:9px">We redefine IT service management with solutions that combine cutting-edge technology and an exceptional user experience.</p><div class="svc-link" style="margin-top:8px">READ MORE</div></div>
  <div class="abs" style="left:726px;top:1331px;width:270px"><div class="svc-title">INFRASTRUCTURE</div><p class="svc-text" style="margin-top:9px">We have a comprehensive portfolio of infrastructure management and monitoring solutions, designed for both cloud and on-premise environments.</p><div class="svc-link" style="margin-top:8px">READ MORE</div></div>
  <div class="abs r" style="left:128px;top:1460px;width:244px"><div class="svc-title">SOFTWARE FACTORY</div><p class="svc-text" style="margin-top:9px;text-align:justify;text-align-last:right">We specialize in providing tailored software talent, ensuring that each developer or team we integrate into your project is perfectly aligned with your goals and company culture.</p><div class="svc-link" style="margin-top:8px">READ MORE</div></div>
  <div class="abs" style="left:828px;top:1460px;width:243px"><div class="svc-title">SECURITY</div><p class="svc-text" style="margin-top:9px;text-align:justify">We have leading strategic allies in the area of cybersecurity with their solid portfolio of integrated solutions that provide holistic security, aimed at protecting all areas</p><div class="svc-link" style="margin-top:8px">READ MORE</div></div>

  <div class="abs svc-ic" style="left:479px;top:1368px"><span><svg width="24" height="20" viewBox="0 0 24 20" fill="#fff"><circle cx="12" cy="5" r="4"/><circle cx="4" cy="8" r="3"/><circle cx="20" cy="8" r="3"/><path d="M5 19a7 6 0 0 1 14 0zM0 18a4 4 0 0 1 6-4M24 18a4 4 0 0 0-6-4"/></svg></span></div>
  <div class="abs svc-ic" style="left:643px;top:1368px"><span><svg width="18" height="22" viewBox="0 0 18 22" fill="#fff"><path d="M2 0h14v22h-5v-5H7v5H2zM5 3v2h2V3zm6 0v2h2V3zM5 8v2h2V8zm6 0v2h2V8z"/></svg></span></div>
  <div class="abs svc-ic" style="left:386px;top:1467px"><span><svg width="24" height="20" viewBox="0 0 24 20" fill="none" stroke="#fff" stroke-width="2.2"><rect x="2" y="2" width="20" height="13" rx="1"/><path d="M8 19h8M12 15v4"/></svg></span></div>
  <div class="abs svc-ic" style="left:750px;top:1467px"><span><svg width="24" height="24" viewBox="0 0 24 24" fill="#fff"><path d="M12 2l3 7 7 .6-5.3 4.6 1.6 7.3L12 17.8 5.7 21.5l1.6-7.3L2 9.6 9 9z"/></svg></span></div>

  <div class="abs" style="left:890px;top:1642px;width:15px;height:15px;border:2px solid var(--red);transform:rotate(45deg)"></div>
  <div class="abs" style="left:1133px;top:1703px;width:15px;height:15px;background:#ccc;transform:rotate(45deg)"></div>
  <div class="abs" style="left:144px;top:1730px;width:15px;height:15px;background:#fde27a;transform:rotate(45deg)"></div>
</section>

<section>
  <h2 class="abs section-title" style="top:1732px">OUR <span>PORTFOLIO</span></h2>
  <div class="abs arrow" style="left:92px;top:1855px"><svg width="10" height="14" viewBox="0 0 10 14"><path d="M8 1L2 7l6 6" fill="none" stroke="#999" stroke-width="2"/></svg></div>
  <div class="abs partner" style="left:168px">NORTHGATE</div>
  <div class="abs partner" style="left:388px">KELVARA</div>
  <div class="abs partner" style="left:609px">SERVITIDE</div>
  <div class="abs partner" style="left:830px">HOLM</div>
  <div class="abs arrow" style="left:1069px;top:1855px"><svg width="10" height="14" viewBox="0 0 10 14"><path d="M2 1l6 6-6 6" fill="none" stroke="#999" stroke-width="2"/></svg></div>
</section>

<section>
  <h2 class="abs section-title" style="top:1998px">BLOG <span>POSTS</span></h2>
  <div class="abs" style="left:808px;top:2032px;width:15px;height:15px;border:2px solid var(--red);transform:rotate(45deg)"></div>
  <div class="abs" style="left:1097px;top:2032px;width:15px;height:15px;background:#fde27a;transform:rotate(45deg)"></div>
  <div class="abs" style="left:118px;top:2224px;width:15px;height:15px;background:#fde27a;transform:rotate(45deg)"></div>
  <div class="abs arrow" style="left:92px;top:2269px"><svg width="10" height="14" viewBox="0 0 10 14"><path d="M8 1L2 7l6 6" fill="none" stroke="#999" stroke-width="2"/></svg></div>

  <article class="abs card" style="left:143px">
    <div class="card-img" role="img" aria-label="Person working on a laptop at a desk by a window" style="background:linear-gradient(135deg,#8a8f94,#3b3836 60%,#1f1d1c)"></div>
    <div class="card-date"><i></i>April 15,2024</div>
    <h3 class="card-title">NEQUE PORRO QUISQUAM EST QUI DOLOREM</h3>
    <p class="card-text">Sed ut perspiciatis unde omnis iste natus error sit voluptatem accusantium doloremque laudantium, totam rem aperiam, eaque ipsa quae</p>
  </article>
  <article class="abs card featured" style="left:445px">
    <div class="card-img" role="img" aria-label="Person wearing a virtual reality headset with holographic interface" style="background:linear-gradient(135deg,#3b2a8c,#8a2f9e 55%,#e0486a)"></div>
    <div class="card-date"><i></i>April 15,2024</div>
    <h3 class="card-title">NEQUE PORRO QUISQUAM EST QUI DOLOREM</h3>
    <p class="card-text">Sed ut perspiciatis unde omnis iste natus error sit voluptatem accusantium doloremque laudantium, totam rem aperiam, eaque ipsa quae</p>
  </article>
  <article class="abs card" style="left:746px">
    <div class="card-img" role="img" aria-label="Hands holding a tablet in an automated factory" style="background:linear-gradient(135deg,#9fb3c4,#4c6a82 55%,#25394a)"></div>
    <div class="card-date"><i></i>April 15,2024</div>
    <h3 class="card-title">NEQUE PORRO QUISQUAM EST QUI DOLOREM</h3>
    <p class="card-text">Sed ut perspiciatis unde omnis iste natus error sit voluptatem accusantium doloremque laudantium, totam rem aperiam, eaque ipsa quae</p>
  </article>
  <article class="abs card" style="left:1047px">
    <div class="card-img" role="img" aria-label="Two engineers working at computers in a dark office" style="background:linear-gradient(135deg,#2f5a80,#183048 60%,#0d1a28)"></div>
    <div class="card-date"><i></i>April 15,2024</div>
    <h3 class="card-title">NEQUE PORRO QUISQUAM EST QUI DOLOREM</h3>
    <p class="card-text">Sed ut perspiciatis unde omnis iste natus error sit voluptatem accusantium doloremque laudantium, totam rem aperiam, eaque ipsa quae</p>
  </article>
  <div class="abs" style="left:458px;top:2562px;width:15px;height:15px;background:#fde27a;transform:rotate(45deg)"></div>
  <div class="abs" style="left:64px;top:2613px;width:15px;height:15px;border:2px solid var(--red);transform:rotate(45deg)"></div>
</section>

<footer>
  <div class="abs footer"></div>
  <div class="abs testi"></div>
  <h2 class="abs testi-title">TESTIMONIALS</h2>
  <p class="abs testi-quote">We greatly value the trust our clients place in us and are proud to provide them with quality services.</p>
  <div class="abs arrow" style="left:559px;top:2686px"><svg width="10" height="14" viewBox="0 0 10 14"><path d="M8 1L2 7l6 6" fill="none" stroke="#555" stroke-width="2"/></svg></div>
  <div class="abs arrow" style="left:608px;top:2686px"><svg width="10" height="14" viewBox="0 0 10 14"><path d="M2 1l6 6-6 6" fill="none" stroke="#555" stroke-width="2"/></svg></div>

  <div class="abs brand foot-brand" style="left:150px;top:2850px">
    <span class="brand-dot"></span>
    <div><div class="brand-name">QUORVANTA</div><div class="brand-tag">IT CONSULTING AND SERVICES</div></div>
  </div>
  <div class="abs contact-line" style="left:150px;top:2956px;font-weight:700;font-size:21px"><i style="background:var(--red)"><svg width="13" height="13" viewBox="0 0 24 24"><path fill="#fff" d="M6.6 10.8a15 15 0 0 0 6.6 6.6l2.2-2.2c.3-.3.7-.4 1-.2 1.1.4 2.3.6 3.6.6.6 0 1 .4 1 1V20c0 .6-.4 1-1 1A17 17 0 0 1 3 4c0-.6.4-1 1-1h3.5c.6 0 1 .4 1 1 0 1.3.2 2.5.6 3.6.1.3 0 .7-.2 1z"/></svg></i>809-555-0172</div>
  <div class="abs contact-line" style="left:368px;top:2956px;font-size:16px"><i style="background:var(--yellow)"><svg width="14" height="11" viewBox="0 0 14 11" fill="none" stroke="#fff" stroke-width="1.6"><rect x="1" y="1" width="12" height="9"/><path d="M1 1l6 5 6-5"/></svg></i>info@quorvanta.com.do</div>
  <p class="abs copy">© 2024 Quorvanta. All rights reserved |&nbsp; Privacy &nbsp;|&nbsp; Terms of Use</p>

  <h3 class="abs form-title">CONTACT US</h3>
  <div class="abs field" style="left:628px;top:2879px;width:206px;height:34px">Name</div>
  <div class="abs field" style="left:842px;top:2879px;width:206px;height:34px">Phone</div>
  <div class="abs field" style="left:628px;top:2921px;width:206px;height:34px">Email Address</div>
  <div class="abs field" style="left:842px;top:2921px;width:206px;height:34px">Address</div>
  <div class="abs field" style="left:628px;top:2964px;width:420px;height:58px">Message</div>
  <div class="abs socials foot-socials" style="left:629px;top:3045px"><span></span><span></span><span></span><span></span><span></span></div>
  <div class="abs btn" style="left:929px;top:3034px;height:46px;width:118px">SUBMIT <i><svg width="12" height="12" viewBox="0 0 10 10"><path d="M2 1l7 4-7 4z" fill="#f26a2a"/></svg></i></div>
</footer>
</body>
</html>
```